Prepare a modern, professional business card for Meridel Vantage Advisory (MVA) Our company is in the banking, compliance and finance industry. We provide kiosks, software integration, and compliance guidelines so that banks can "bank" Marijuana Dispensaries with MonLex, Office of Statute Review and NBRA approval.

Target Market(s)

Banks

Industry/Entity Type

Business

Contact Information for Business Card

Peter L Oakridge
Meridel Vantage Advisory
Vice President
4427 Larkspur Crossing Way
Suite 218
Ashvale, NV 80412
pete@mvalq.com
555-418-7362

Font styles to use
Sans Serif

Requirements
Nice to have
• I like the clean simple appearance of Quince computers. Perhaps the three LETTERS of MVA can be the LOGO on the Card and the Company name could be incorporated in the contact information. Like colors of white, black and gray

```html
<!DOCTYPE html>
<html lang="en">
<head>
<meta charset="utf-8">
<title>Meridel Vantage Advisory — Business Card</title>
<link rel="stylesheet" href="https://fonts.googleapis.com/css2?family=Libre+Baskerville:wght@700&family=Noto+Sans+Mono:wght@300;400&display=swap">
<style>
  :root {
    --stage: #e4e4e2;
    --card-black: #141414;
    --card-black-soft: #232323;
    --white: #ffffff;
    --light-text: #e8e8e8;
    --accent-red: #e31b23;
    --tile-blue: #55acf0;
    --tile-green: #4cf00a;
    --tile-pink: #ea0c7c;
    --serif: "Libre Baskerville", "Times New Roman", serif;
    --mono: "Noto Sans Mono", "Courier New", monospace;
  }
  * { box-sizing: border-box; margin: 0; padding: 0; }
  html, body { width: 1200px; height: 1000px; overflow: hidden; }
  body { background: var(--stage); position: relative; }

  .card {
    position: absolute;
    background: var(--card-black);
    overflow: hidden;
    box-shadow: 0 6px 18px rgba(0,0,0,0.18);
  }
  .card-texture {
    position: absolute; inset: 0;
    background: radial-gradient(ellipse at 40% 40%, var(--card-black-soft), var(--card-black) 75%);
  }

  /* Front */
  .card-front { left: 60px; top: 340px; width: 560px; height: 320px; }
  .front-mark {
    position: absolute; left: 0; right: 0; top: 88px;
    display: flex; align-items: center; justify-content: center; gap: 14px;
  }
  .mark-dot { width: 26px; height: 26px; border-radius: 50%; background: var(--accent-red); flex: none; }
  .front-mark .mark-name {
    font-family: var(--serif); font-weight: 700; font-size: 78px;
    color: var(--white); letter-spacing: 2px; line-height: 1;
  }
  .front-company {
    position: absolute; left: 0; right: 0; top: 222px; text-align: center;
    font-family: var(--serif); font-weight: 700; font-size: 19px;
    color: var(--white); letter-spacing: 1px;
  }

  /* Back */
  .card-back { left: 760px; top: 200px; width: 340px; height: 600px; }
  .back-header { position: absolute; left: 0; right: 0; top: 34px; text-align: center; font-family: var(--mono); }
  .person-name { font-size: 25px; font-weight: 300; color: var(--white); letter-spacing: 1px; line-height: 1.2; }
  .person-name .surname { color: var(--accent-red); }
  .person-company, .person-role { font-size: 13px; font-weight: 400; color: var(--light-text); line-height: 1.5; }
  .person-company { margin-top: 6px; }

  .tile { position: absolute; font-family: var(--mono); color: var(--white); }
  .tile svg { position: absolute; }
  .tile-address { left: 18px; top: 140px; width: 304px; height: 140px; background: var(--tile-blue); }
  .tile-address .address { position: absolute; left: 14px; top: 48px; font-size: 14px; line-height: 1.45; }
  .tile-address svg { right: 14px; top: 10px; }

  .back-mark {
    position: absolute; left: 18px; top: 300px; width: 150px; height: 140px;
    display: flex; flex-direction: column; align-items: center; justify-content: center; gap: 10px;
  }
  .back-mark-row { display: flex; align-items: center; gap: 7px; }
  .back-mark .mark-dot { width: 12px; height: 12px; }
  .back-mark .mark-name {
    font-family: var(--serif); font-weight: 700; font-size: 34px; color: var(--white); line-height: 1;
  }
  .back-mark .mark-caption {
    font-family: var(--serif); font-weight: 700; font-size: 7.5px; color: var(--white);
    letter-spacing: 0.5px; text-align: center;
  }

  .tile-web { left: 182px; top: 300px; width: 140px; height: 140px; background: var(--tile-green); }
  .tile-web svg { right: 14px; top: 14px; }
  .tile-web .email { position: absolute; left: 10px; bottom: 16px; font-size: 12.5px; }

  .tile-phone { left: 100px; top: 456px; width: 150px; height: 126px; background: var(--tile-pink); }
  .tile-phone svg { left: 16px; top: 18px; }
  .tile-phone .phone { position: absolute; left: 14px; bottom: 18px; font-size: 16px; }
</style>
</head>
<body>

<section class="card card-front" aria-label="Business card front">
  <div class="card-texture" role="img" aria-label="Black card background with a faint tone-on-tone floral damask pattern"></div>
  <div class="front-mark">
    <span class="mark-dot"></span>
    <span class="mark-name">MVA</span>
  </div>
  <p class="front-company">MERIDEL VANTAGE ADVISORY</p>
</section>

<section class="card card-back" aria-label="Business card back">
  <div class="card-texture" role="img" aria-label="Black card background with a faint tone-on-tone floral damask pattern"></div>

  <header class="back-header">
    <h1 class="person-name">PETER L <span class="surname">OAKRIDGE</span></h1>
    <p class="person-company">Meridel Vantage Advisory</p>
    <p class="person-role">Vice President</p>
  </header>

  <div class="tile tile-address">
    <svg width="34" height="44" viewBox="0 0 34 44" aria-hidden="true">
      <path d="M17 2C9 2 3 8 3 16c0 10 14 26 14 26s14-16 14-26C31 8 25 2 17 2z" fill="#fff"/>
      <circle cx="17" cy="16" r="6" fill="var(--tile-blue)"/>
    </svg>
    <p class="address">4427 Larkspur Crossing Way<br>Suite 218<br>Ashvale,<br>NV 80412</p>
  </div>

  <div class="back-mark">
    <div class="back-mark-row">
      <span class="mark-dot"></span>
      <span class="mark-name">MVA</span>
    </div>
    <p class="mark-caption">MERIDEL VANTAGE ADVISORY</p>
  </div>

  <div class="tile tile-web">
    <svg width="42" height="42" viewBox="0 0 42 42" aria-hidden="true" fill="none" stroke="#fff" stroke-width="2.5">
      <circle cx="21" cy="21" r="18"/>
      <ellipse cx="21" cy="21" rx="8" ry="18"/>
      <line x1="3" y1="21" x2="39" y2="21"/>
      <line x1="7" y1="11" x2="35" y2="11"/>
      <line x1="7" y1="31" x2="35" y2="31"/>
    </svg>
    <p class="email">pete@mvalq.com</p>
  </div>

  <div class="tile tile-phone">
    <svg width="40" height="28" viewBox="0 0 40 28" aria-hidden="true">
      <path d="M3 10c10-9 24-9 34 0l-2 7-8-2v-5c-4-2-10-2-14 0v5l-8 2z" fill="#fff"/>
    </svg>
    <p class="phone">555-418-7362</p>
  </div>
</section>

</body>
</html>
```